Offshore Energy Projects Management Consultancy needs a business card design

Logo available. We provide teams to deliver engineering consultancy, project management and delivery teams mainly in the offshore renewables sector. The company is all about bringing the right people to a project to deliver the scope.

The business card will be used for all staff.

The business card should be quite simple, vibrant and uncluttered but convey experience, enthusiasm and integration.

Target Market(s)

Energy Project Developers and Tier 1 construction companies

Contact Information for Business Card

Logo should be on the back of the card. I'm happy for the designer to play with the colour of the logo and background colour.

Front of the card should convey all the must have information in a clear and professional manner but without being overly traditional.

Colors

Designer to choose colors to be used in the design.

Requirements
Must have
• Land Line Tel Number, Mobile Tel Number, Email, business address, web address.

```html
<!DOCTYPE html>
<html lang="en">
<head>
<meta charset="utf-8">
<title>Tideline Projects Group — Business Card</title>
<link rel="stylesheet" href="https://fonts.googleapis.com/css2?family=Open+Sans:wght@400;600;700&display=swap">
<style>
  :root {
    --backdrop: #3a322d;
    --card: #121214;
    --card-edge: #1c1c1f;
    --accent: #2a8fe0;
    --text-light: #c9c9cc;
    --divider: #2c2c30;
    --pattern-a: #17171a;
    --pattern-b: #1e1e22;
  }
  * { box-sizing: border-box; margin: 0; padding: 0; }
  html, body { width: 1200px; height: 844px; overflow: hidden; }
  body {
    background: var(--backdrop);
    font-family: "Open Sans", Arial, sans-serif;
    position: relative;
  }
  .card {
    position: absolute;
    top: 272px;
    width: 525px;
    height: 300px;
    background: var(--card);
    border: 1px solid var(--card-edge);
    border-radius: 3px;
    overflow: hidden;
  }
  .card--front { left: 50px; }
  .card--back { left: 625px; }

  .brand {
    position: absolute;
    left: 34px;
    top: 112px;
    width: 220px;
    display: flex;
    align-items: center;
    gap: 12px;
  }
  .brand__dot {
    flex: 0 0 auto;
    width: 34px;
    height: 34px;
    border-radius: 50%;
    background: var(--accent);
  }
  .brand__name {
    color: var(--accent);
    font-weight: 700;
    font-size: 21px;
    line-height: 1.15;
    text-transform: uppercase;
  }
  .divider {
    position: absolute;
    left: 272px;
    top: 60px;
    width: 1px;
    height: 180px;
    background: var(--divider);
  }
  .contact {
    position: absolute;
    left: 292px;
    top: 62px;
    color: var(--text-light);
    font-size: 13.5px;
    line-height: 19px;
  }
  .contact__name {
    color: var(--accent);
    font-weight: 700;
    font-size: 17px;
    line-height: 20px;
    text-transform: uppercase;
  }
  .contact__role { margin-bottom: 4px; }
  .contact__list { list-style: none; }
  .contact__list li { display: flex; align-items: center; gap: 8px; }
  .contact__list svg { width: 11px; height: 11px; fill: var(--accent); flex: 0 0 auto; }
  .contact__address { margin-top: 10px; }

  .pattern {
    position: absolute;
    inset: 0;
    background: linear-gradient(135deg, var(--pattern-a), var(--pattern-b) 50%, var(--pattern-a));
  }
  .back-brand {
    position: absolute;
    left: 50%;
    top: 50%;
    transform: translate(-50%, -50%);
    display: flex;
    align-items: center;
    gap: 8px;
    color: var(--accent);
    font-weight: 700;
    font-size: 14px;
    text-transform: uppercase;
    white-space: nowrap;
  }
  .back-brand__dot { width: 14px; height: 14px; border-radius: 50%; background: var(--accent); }
</style>
</head>
<body>
  <section class="card card--front" aria-label="Business card front">
    <div class="brand">
      <span class="brand__dot"></span>
      <span class="brand__name">Tideline<br>Projects Group</span>
    </div>
    <div class="divider"></div>
    <div class="contact">
      <p class="contact__name">Daniel Harper</p>
      <p class="contact__role">Managing Director</p>
      <ul class="contact__list">
        <li><svg viewBox="0 0 12 12" aria-hidden="true"><path d="M1 3c0-1 1-2 2-2h1l1 3-1 1c1 2 2 3 4 4l1-1 3 1v1c0 1-1 2-2 2C5 12 0 7 1 3z"/></svg>020-555 0142</li>
        <li><svg viewBox="0 0 12 12" aria-hidden="true"><path d="M3 0h6a1 1 0 0 1 1 1v10a1 1 0 0 1-1 1H3a1 1 0 0 1-1-1V1a1 1 0 0 1 1-1zm0 2v7h6V2z"/></svg>077-555 0187</li>
        <li><svg viewBox="0 0 12 12" aria-hidden="true"><path d="M0 2h12v1L6 7 0 3zm0 2.5 6 4 6-4V10H0z"/></svg>hello@tidelinegroup.co</li>
        <li><svg viewBox="0 0 12 12" aria-hidden="true"><circle cx="6" cy="6" r="5.5"/></svg>www.tidelinegroup.co</li>
      </ul>
      <p class="contact__address">48 Quayside Wharf Road<br>Harbourton, HT4 7QP.</p>
    </div>
  </section>

  <section class="card card--back" aria-label="Business card back">
    <div class="pattern" role="img" aria-label="Faint repeated brand-name pattern across a black background"></div>
    <div class="back-brand">
      <span class="back-brand__dot"></span>
      <span>Tideline Projects Group</span>
    </div>
  </section>
</body>
</html>
```